Specialised investor in e-mobility and energy wants business card design

We need a business card design that fits our existing corporate design. <The look and feel must be 'sharp'/'clean', dynamic, communicate momentum, professionalism etc (as one would imagine from a firm in the financial sector). We like the idea of a reverse-side of the card that includes the logo, and the name and contact details on the other. We expect the deliverable to be whatever format might be required to be able to get cards printed directly by a service such as tandor press. Our website is www.orm.capital

```html
<!DOCTYPE html>
<html lang="en">
<head>
<meta charset="utf-8">
<title>ORM Capital – Business Card</title>
<link href="https://fonts.googleapis.com/css2?family=Roboto:wght@400;500&display=swap" rel="stylesheet">
<style>
  :root {
    --backdrop: #d2d3d5;
    --card: #ffffff;
    --green-dark: #2d4a22;
    --green-light: #7ab648;
  }
  * { margin: 0; padding: 0; box-sizing: border-box; }
  html, body {
    width: 900px;
    height: 1200px;
    overflow: hidden;
    background: var(--backdrop);
    font-family: "Roboto", Arial, sans-serif;
  }
  .card {
    position: absolute;
    left: 165px;
    width: 570px;
    height: 374px;
    background: var(--card);
  }
  .card--front { top: 190px; }
  .card--back { top: 636px; }

  .brand {
    position: absolute;
    display: flex;
    align-items: center;
    gap: 14px;
    color: var(--green-dark);
    font-weight: 400;
    white-space: nowrap;
  }
  .brand__dot {
    border-radius: 50%;
    background: var(--green-light);
  }
  .card--front .brand {
    left: 50%;
    top: 50%;
    transform: translate(-50%, -50%);
    font-size: 52px;
  }
  .card--front .brand__dot { width: 22px; height: 22px; }
  .card--back .brand {
    right: 32px;
    top: 40px;
    font-size: 40px;
    gap: 11px;
  }
  .card--back .brand__dot { width: 17px; height: 17px; }

  .holder {
    position: absolute;
    left: 33px;
    top: 205px;
  }
  .holder__name {
    color: var(--green-light);
    font-size: 23px;
    font-weight: 500;
    line-height: 1.1;
  }
  .holder__role {
    color: var(--green-dark);
    font-size: 14px;
    margin-top: 4px;
    letter-spacing: 0.3px;
  }
  .holder__rule {
    width: 48px;
    height: 3px;
    background: var(--green-light);
    margin-top: 8px;
  }
  .contact {
    list-style: none;
    margin-top: 14px;
  }
  .contact li {
    display: flex;
    align-items: center;
    gap: 7px;
    color: var(--green-dark);
    font-size: 15px;
    letter-spacing: 0.5px;
    height: 22px;
  }
  .contact svg { width: 12px; height: 12px; fill: var(--green-light); flex: none; }
</style>
</head>
<body>
  <section class="card card--front">
    <div class="brand"><span class="brand__dot"></span>ORM Capital</div>
  </section>

  <section class="card card--back">
    <div class="brand"><span class="brand__dot"></span>ORM Capital</div>

    <div class="holder">
      <p class="holder__name">Lukas Brenner</p>
      <p class="holder__role">Partner</p>
      <div class="holder__rule"></div>
      <ul class="contact">
        <li>
          <svg viewBox="0 0 24 24" aria-hidden="true"><path d="M6.6 10.8a15.1 15.1 0 0 0 6.6 6.6l2.2-2.2a1 1 0 0 1 1-.25 11.4 11.4 0 0 0 3.6.57 1 1 0 0 1 1 1V20a1 1 0 0 1-1 1A17 17 0 0 1 3 4a1 1 0 0 1 1-1h3.5a1 1 0 0 1 1 1c0 1.25.2 2.45.57 3.57a1 1 0 0 1-.25 1z"/></svg>
          +41 79480 2157
        </li>
        <li>
          <svg viewBox="0 0 24 24" aria-hidden="true"><path d="M2 5h20v14H2z M2 5l10 8 10-8" /></svg>
          lukas@orm.capital
        </li>
        <li>
          <svg viewBox="0 0 24 24" aria-hidden="true"><path d="M12 2a10 10 0 1 0 0 20 10 10 0 0 0 0-20zm6.9 6h-3a15.6 15.6 0 0 0-1.4-3.6A8 8 0 0 1 18.9 8zM12 4c.8 1.2 1.5 2.5 1.9 4h-3.8c.4-1.5 1.1-2.8 1.9-4zM4.3 14a8 8 0 0 1 0-4h3.4a16 16 0 0 0 0 4zm.8 2h3a15.6 15.6 0 0 0 1.4 3.6A8 8 0 0 1 5.1 16zm3-8h-3a8 8 0 0 1 4.3-3.6A15.6 15.6 0 0 0 8.1 8zM12 20c-.8-1.2-1.5-2.5-1.9-4h3.8c-.4 1.5-1.1 2.8-1.9 4zm2.3-6H9.7a14.7 14.7 0 0 1 0-4h4.6a14.7 14.7 0 0 1 0 4zm.3 5.6a15.6 15.6 0 0 0 1.4-3.6h3a8 8 0 0 1-4.4 3.6zm1.7-5.6a16 16 0 0 0 0-4h3.4a8 8 0 0 1 0 4z"/></svg>
          www.orm.capital
        </li>
      </ul>
    </div>
  </section>
</body>
</html>
```